Signage for a store*

logo on the two sides of the sign
in the middle is the name of the store witch is KORVELO
at the bottom of the two logos, one side for location/address and the other side is contact details phone number is 718-392-6170 address is 7342 THE SIGN WILL BEE 15 FEET BY 4 FEET I WOULD LIKE THAT THE
BACKGROUND OF THE SIGN SHOULD HAVE A NICE COLOR BASE
THAT GOES FOR A WINE STORE

```html
<!DOCTYPE html>
<html lang="en">
<head>
<meta charset="utf-8">
<title>KORVELO – Store Sign</title>
<link rel="stylesheet" href="https://fonts.googleapis.com/css2?family=Bigelow+Rules&family=Federo&display=swap">
<style>
  :root {
    --stage: #000000;
    --cream: #f1ece0;
    --leaf-tone: #e9e1cf;
    --wine: #a12645;
    --gold: #b38a2e;
  }
  * { margin: 0; padding: 0; box-sizing: border-box; }
  html, body {
    width: 1200px;
    height: 675px;
    overflow: hidden;
    background: var(--stage);
  }
  .board {
    position: relative;
    width: 1200px;
    height: 675px;
  }
  .sign {
    position: absolute;
    left: 104px;
    width: 993px;
    height: 264px;
    overflow: hidden;
  }
  .sign--framed { top: 41px; }
  .sign--plain { top: 362px; }

  .sign__backdrop {
    position: absolute;
    inset: 0;
    background: radial-gradient(ellipse at 50% 50%, var(--cream) 55%, var(--leaf-tone) 100%);
  }
  .sign__frame {
    position: absolute;
    inset: 7px;
    border: 2px solid var(--wine);
  }

  .emblem {
    position: absolute;
    top: 28px;
    width: 116px;
    height: 150px;
    display: flex;
    flex-direction: column;
    align-items: center;
    justify-content: center;
    gap: 10px;
  }
  .emblem--left { left: 43px; }
  .emblem--right { left: 830px; }
  .emblem__dot {
    width: 44px;
    height: 44px;
    border-radius: 50%;
    background: var(--wine);
  }
  .emblem__name {
    font-family: "Federo", sans-serif;
    font-size: 23px;
    line-height: 1;
    color: var(--wine);
    letter-spacing: 0.5px;
  }

  .storename {
    position: absolute;
    left: 233px;
    top: 22px;
    width: 529px;
    height: 226px;
  }
  .storename text {
    font-family: "Bigelow Rules", fantasy;
    font-size: 250px;
  }
  .storename__shadow { fill: var(--gold); }
  .storename__face { fill: var(--wine); }

  .detail {
    position: absolute;
    top: 200px;
    font-family: "Bigelow Rules", fantasy;
    font-size: 44px;
    line-height: 1;
    color: var(--wine);
    white-space: nowrap;
    letter-spacing: 1px;
  }
  .detail--phone { left: 25px; }
  .detail--address { right: 25px; }
  .detail__number { color: var(--gold); }
</style>
</head>
<body>
<main class="board">

  <section class="sign sign--framed" aria-label="Sign with frame">
    <div class="sign__backdrop" role="img" aria-label="Cream background with a faint vine leaf pattern"></div>
    <div class="sign__frame"></div>

    <div class="emblem emblem--left">
      <span class="emblem__dot"></span>
      <span class="emblem__name">KORVELO</span>
    </div>

    <svg class="storename" viewBox="0 0 529 226" aria-label="KORVELO">
      <text class="storename__shadow" x="-3" y="200" textLength="529" lengthAdjust="spacingAndGlyphs">KORVELO</text>
      <text class="storename__face" x="0" y="198" textLength="529" lengthAdjust="spacingAndGlyphs">KORVELO</text>
    </svg>

    <div class="emblem emblem--right">
      <span class="emblem__dot"></span>
      <span class="emblem__name">KORVELO</span>
    </div>

    <p class="detail detail--phone">718-392-6170</p>
    <p class="detail detail--address">ADDRESS <span class="detail__number">(7342)</span></p>
  </section>

  <section class="sign sign--plain" aria-label="Sign without frame">
    <div class="sign__backdrop" role="img" aria-label="Cream background with a faint vine leaf pattern"></div>

    <div class="emblem emblem--left">
      <span class="emblem__dot"></span>
      <span class="emblem__name">KORVELO</span>
    </div>

    <svg class="storename" viewBox="0 0 529 226" aria-label="KORVELO">
      <text class="storename__face" x="0" y="198" textLength="529" lengthAdjust="spacingAndGlyphs">KORVELO</text>
    </svg>

    <div class="emblem emblem--right">
      <span class="emblem__dot"></span>
      <span class="emblem__name">KORVELO</span>
    </div>

    <p class="detail detail--phone">718-392-6170</p>
    <p class="detail detail--address">ADDRESS <span class="detail__number">(7342)</span></p>
  </section>

</main>
</body>
</html>
```